Hunting Ethics Organization Needs a Web Design with Logo Refresh

This project involves the creation of a website design including the homepage design, inside page design, and logo refinements. Our organization is Talvera, and we are a not-for-profit hunting ethics organization.
The focus of the new website design is to bring attention the mission of our organization, provide an overview of the areas where our organization deploys its resources to support the modern hunter, and to encourage visitors to support our organization by donating in support of the organization’s mission.
The winning design will be implemented in Wordpress by our in-house team. If you have questions about how any particular design element may translate to Wordpress, please feel free to post questions in response to this brief. In general, however, we’re more focused on the evolution and delivery of a strong overall design aesthetic – we’ll shoulder the responsibility of how we translate that design into Wordpress.
See attached design brief for full details.

```html
<!DOCTYPE html>
<html lang="en">
<head>
<meta charset="utf-8">
<title>Talvera — Hunting Ethics</title>
<link href="https://fonts.googleapis.com/css2?family=Open+Sans:wght@400;600;700&family=PT+Sans+Narrow:wght@400;700&display=swap" rel="stylesheet">
<style>
  :root {
    --backdrop: #414141;
    --topbar: #e9e9e9;
    --white: #ffffff;
    --brand-text: #3a3a3a;
    --brand-dot: #9b9b9b;
    --nav-text: #8a8a8a;
    --hero-warm: #d89a2a;
    --hero-dark: #3a2a12;
    --panel: #3b3020;
    --panel-text: #f3efe6;
    --section-bg: #f1f1f1;
    --section-fade: #f9f9f9;
    --head-dark: #3a3a3a;
    --head-light: #9b9b9b;
    --link-gold: #c8860a;
    --band: #e4e4e4;
    --footer: #dcdcdc;
    --footer-text: #4a4a4a;
    --bottom: #a3a3a3;
    --icon: #3f3f3f;
  }
  * { box-sizing: border-box; margin: 0; padding: 0; }
  html, body { width: 849px; height: 1200px; overflow: hidden; }
  body { background: var(--backdrop); font-family: "Open Sans", Arial, sans-serif; position: relative; }
  .page { position: absolute; left: 37px; top: 0; width: 775px; height: 997px; box-shadow: 0 0 12px rgba(0,0,0,.5); }
  .abs { position: absolute; }

  .utility-bar { left: 0; top: 0; width: 775px; height: 27px; background: var(--topbar); font-size: 12px; color: #666; text-align: right; padding: 5px 8px 0 0; }
  .utility-bar span { color: #aaa; margin: 0 2px; }

  .site-header { left: 0; top: 27px; width: 775px; height: 73px; background: var(--white); }
  .brand-dot { left: 24px; top: 18px; width: 36px; height: 36px; border-radius: 50%; background: var(--brand-dot); }
  .brand-name { left: 70px; top: 17px; font-weight: 600; font-size: 28px; line-height: 38px; color: var(--brand-text); }

  .main-nav { left: 0; top: 0; width: 775px; height: 73px; }
  .nav-item { position: absolute; top: 20px; transform: translateX(-50%); text-align: center; font-size: 8.5px; color: var(--nav-text); white-space: nowrap; letter-spacing: .2px; }
  .nav-item svg { display: block; margin: 0 auto 6px; }

  .hero { left: 0; top: 100px; width: 775px; height: 273px; }
  .hero-photo { left: 0; top: 0; width: 534px; height: 273px; background: radial-gradient(ellipse at 70% 35%, #f3c451 0%, var(--hero-warm) 35%, #8a5a17 70%, var(--hero-dark) 100%); }
  .hero-panel { left: 534px; top: 0; width: 241px; height: 273px; background: var(--panel); padding: 32px 24px 0 24px; color: var(--panel-text); }
  .hero-panel h1 { font-family: "PT Sans Narrow", Arial, sans-serif; font-weight: 400; font-size: 17px; line-height: 18px; text-transform: uppercase; margin-bottom: 18px; }
  .hero-panel p { font-size: 9.5px; line-height: 15.5px; text-align: justify; }

  .gap { left: 0; top: 373px; width: 775px; height: 11px; background: #555; }

  .focus { left: 0; top: 384px; width: 775px; height: 305px; background: linear-gradient(var(--section-bg), var(--section-fade)); }
  .focus-title { left: 0; top: 30px; width: 775px; text-align: center; font-family: "PT Sans Narrow", Arial, sans-serif; text-transform: uppercase; }
  .focus-title .line1 { display: block; font-size: 24px; line-height: 28px; color: var(--head-light); }
  .focus-title .line2 { display: block; font-size: 17px; line-height: 22px; color: var(--head-light); }
  .focus-title b { color: var(--head-dark); }
  .area { top: 120px; width: 178px; }
  .area h3 { font-family: "PT Sans Narrow", Arial, sans-serif; font-weight: 400; font-size: 11px; color: #444; text-transform: uppercase; margin-bottom: 22px; }
  .area h3.strong { font-weight: 700; }
  .area-photo { width: 178px; height: 65px; }
  .area a { display: block; margin-top: 8px; font-size: 12px; line-height: 19px; color: var(--link-gold); text-decoration: none; }

  .feed-band { left: 0; top: 689px; width: 775px; height: 60px; background: var(--band); }
  .stamp { left: 27px; top: 2px; width: 58px; height: 52px; background: var(--white); border: 3px dotted #d8d8d8; transform: rotate(-6deg); box-shadow: 1px 2px 4px rgba(0,0,0,.2); }
  .stamp-inner { position: absolute; left: 12px; top: 10px; width: 26px; height: 24px; background: #a9a9a9; }

  .site-footer { left: 0; top: 749px; width: 775px; height: 204px; background: var(--footer); color: var(--footer-text); }
  .foot-col { top: 32px; }
  .foot-col h4 { font-family: "PT Sans Narrow", Arial, sans-serif; font-weight: 400; font-size: 14px; color: #333; text-transform: uppercase; }
  .foot-col ol { font-size: 9px; padding-left: 14px; }
  .company-text { width: 174px; font-size: 8.5px; line-height: 15px; text-align: justify; margin-top: 10px; }
  .thumbs { display: grid; grid-template-columns: repeat(3, 45px); gap: 11px 12px; margin: 14px 0 0 17px; }
  .thumb { width: 45px; height: 45px; border: 2px solid #fff; box-shadow: 0 1px 3px rgba(0,0,0,.3); background: #eee; }
  .posts { margin: 8px 0 0 15px; }
  .post-title { font-size: 9px; font-weight: 700; line-height: 18px; color: #333; text-transform: uppercase; width: 170px; }
  .post-date { font-size: 7px; color: #555; margin: 4px 0 8px; display: flex; align-items: center; gap: 6px; }
  .foot-col ol.menu-list { font-size: 12px; line-height: 17px; }
  .menu-list li:nth-child(2) { margin-top: 8px; }
  .menu-list a { color: var(--link-gold); text-decoration: none; }

  .bottom-bar { left: 0; top: 953px; width: 775px; height: 44px; background: var(--bottom); }
  .copyright { left: 16px; top: 15px; font-size: 9px; color: #222; }
  .copyright b { font-size: 11px; }
  .social { right: 17px; top: 12px; display: flex; gap: 6px; }
  .social span { width: 17px; height: 17px; background: var(--icon); border: 2px solid #ddd; }
</style>
</head>
<body>
<div class="page">

  <div class="abs utility-bar">Login <span>|</span> Contact Us</div>

  <header class="abs site-header">
    <div class="abs brand-dot"></div>
    <div class="abs brand-name">Talvera</div>

    <nav class="abs main-nav">
      <div class="nav-item" style="left:371px">
        <svg width="14" height="12" viewBox="0 0 14 12"><path d="M7 0 L14 6 H12 V12 H8.5 V8 H5.5 V12 H2 V6 H0 Z" fill="#8a8a8a"/></svg>ABOUT ▾</div>
      <div class="nav-item" style="left:453px">
        <svg width="15" height="12" viewBox="0 0 15 12"><path d="M0 1 H5 L6.5 3 H13 V5 H3 L0 12 Z M3.5 6 H15 L12 12 H0.5 Z" fill="#8a8a8a"/></svg>HUNTING ETHICS ▾</div>
      <div class="nav-item" style="left:538px">
        <svg width="12" height="13" viewBox="0 0 12 13"><rect x="1" y="0" width="10" height="13" fill="#8a8a8a"/><rect x="5" y="0" width="2" height="6" fill="#fff"/></svg>CONSERVATION</div>
      <div class="nav-item" style="left:621px">
        <svg width="13" height="13" viewBox="0 0 13 13"><circle cx="6.5" cy="6.5" r="3.5" fill="#8a8a8a"/><path d="M6.5 0 V13 M0 6.5 H13 M2 2 L11 11 M11 2 L2 11" stroke="#8a8a8a" stroke-width="1.6"/></svg>GET INVOLVED</div>
      <div class="nav-item" style="left:683px">
        <svg width="12" height="13" viewBox="0 0 12 13"><rect x="0" y="2" width="12" height="11" fill="#8a8a8a"/><rect x="2" y="5" width="8" height="6" fill="#fff"/><rect x="2" y="0" width="2" height="3" fill="#8a8a8a"/><rect x="8" y="0" width="2" height="3" fill="#8a8a8a"/></svg>BLOG</div>
      <div class="nav-item" style="left:736px">
        <svg width="14" height="13" viewBox="0 0 14 13"><rect y="1" width="14" height="11" fill="#8a8a8a"/><path d="M0 1 L7 7 L14 1" stroke="#fff" stroke-width="1.3" fill="none"/></svg>CONTACT</div>
    </nav>
  </header>

  <section class="abs hero">
    <div class="abs hero-photo" role="img" aria-label="Silhouette of a hunter with a shotgun kneeling beside his dog in tall grass at golden sunset"></div>
    <div class="abs hero-panel">
      <h1>Protect the heritage of hunting</h1>
      <p>By becoming a member of TALVERA you're taking an important step to help protect and promote our outdoor heritage. Join today to create a powerful and unified voice for hunters across the country.</p>
    </div>
  </section>

  <div class="abs gap"></div>

  <section class="abs focus">
    <h2 class="abs focus-title">
      <span class="line1"><b>Leaders</b> in setting the example of modern hunter.</span>
      <span class="line2"><b>Protecting the future</b> of hunting</span>
    </h2>

    <article class="abs area" style="left:16px">
      <h3>Hunting Ethics</h3>
      <div class="area-photo" role="img" aria-label="Two hunters silhouetted with a spotting scope against an orange sunset" style="background:linear-gradient(#f7a21c 0%, #e4540c 55%, #1a0d05 80%)"></div>
      <a href="#">Check out our hunting ethics here.</a>
    </article>
    <article class="abs area" style="left:207px">
      <h3>Conservation</h3>
      <div class="area-photo" role="img" aria-label="Bow hunter walking past a weathered tree in a hazy valley" style="background:linear-gradient(100deg,#4a3521 0%,#a68a64 45%,#d9c4a0 75%,#8c6a44 100%)"></div>
      <a href="#">Know more about how to consrve the hunting heritage.</a>
    </article>
    <article class="abs area" style="left:399px">
      <h3>Get Involved</h3>
      <div class="area-photo" role="img" aria-label="Hunter with a gun and his dog silhouetted in a golden field" style="background:radial-gradient(ellipse at 70% 40%,#f1c55a 0%,#c98a26 55%,#5a3a12 100%)"></div>
      <a href="#">Learn how toget involved with our organisation.</a>
    </article>
    <article class="abs area" style="left:590px">
      <h3 class="strong">Donate</h3>
      <div class="area-photo" role="img" aria-label="Two hands meeting in a handshake against a pale sky" style="background:linear-gradient(#b9d2ec 0%,#dfe9f3 55%,#e8c4a8 100%)"></div>
      <a href="#">Check out our hunting ethics here.</a>
    </article>
  </section>

  <div class="abs feed-band">
    <div class="abs stamp"><div class="stamp-inner"></div></div>
  </div>

  <footer class="abs site-footer">
    <div class="abs foot-col" style="left:16px">
      <ol>
        <li><h4>Company</h4></li>
        <li><p class="company-text">Talvera's purpose is to protect the future of hunting by setting the example for the modern hunter. Talvera pursues this mission by providing information to the hunter so that the hunter can educate him/herself on the moral and ethical values, beliefs and principles.</p></li>
      </ol>
    </div>

    <div class="abs foot-col" style="left:206px">
      <ol>
        <li><h4>Photostreaming</h4></li>
      </ol>
      <div class="thumbs">
        <div class="thumb" role="img" aria-label="Street scene photo" style="background:linear-gradient(#8aa2c8,#9b8f9a)"></div>
        <div class="thumb"><svg width="41" height="41" viewBox="0 0 41 41"><rect x="9" y="9" width="23" height="23" fill="none" stroke="#aaa"/><path d="M9 9 L32 32 M32 9 L9 32" stroke="#aaa"/></svg></div>
        <div class="thumb" role="img" aria-label="Outdoor garden photo" style="background:linear-gradient(#7a9a5a,#c0b8a8)"></div>
        <div class="thumb" role="img" aria-label="Ferris wheel photo" style="background:linear-gradient(#5d7fb0,#8aa5c9)"></div>
        <div class="thumb" role="img" aria-label="Landscape photo" style="background:linear-gradient(#c8b89a,#8a7656)"></div>
        <div class="thumb"><svg width="41" height="41" viewBox="0 0 41 41"><rect x="9" y="9" width="23" height="23" fill="none" stroke="#aaa"/><path d="M9 9 L32 32 M32 9 L9 32" stroke="#aaa"/></svg></div>
      </div>
    </div>

    <div class="abs foot-col" style="left:396px">
      <ol>
        <li><h4>Recent Posts</h4></li>
      </ol>
      <div class="posts">
        <p class="post-title">A fresh and nice blog layout: do u like it?</p>
        <p class="post-date"><svg width="8" height="8" viewBox="0 0 8 8"><circle cx="4" cy="4" r="3.3" fill="none" stroke="#444"/><path d="M4 2 V4 H6" stroke="#444" fill="none"/></svg>December 13, 2014</p>
        <p class="post-title">50% off on our registration for the month of January</p>
        <p class="post-date"><svg width="8" height="8" viewBox="0 0 8 8"><circle cx="4" cy="4" r="3.3" fill="none" stroke="#444"/><path d="M4 2 V4 H6" stroke="#444" fill="none"/></svg>December 7, 2014</p>
      </div>
    </div>

    <div class="abs foot-col" style="left:596px">
      <ol class="menu-list">
        <li><h4>Menu</h4></li>
        <li><a href="#">About Talvera</a></li>
        <li><a href="#">Contact Us</a></li>
        <li><a href="#">Donate</a></li>
        <li><a href="#">Blog</a></li>
        <li><a href="#">Login</a></li>
      </ol>
    </div>
  </footer>

  <div class="abs bottom-bar">
    <p class="abs copyright">Copyright <b>Vantor</b> 2010 - Powered by <b>Brightfold Web</b></p>
    <div class="abs social">
      <span></span><span></span><span></span><span></span><span></span><span></span><span></span><span></span>
    </div>
  </div>

</div>
</body>
</html>
```